MR Business Card

I want to create a simple business card.
I am a consultant. I design and develop furniture, lighting and accessories for hospitality and retail brands.
I want the card to be simple and clean. Not too much of a logo - but it needs the basic information shown on the attached file.
Also - I have shown some fonts that I like on the attached file.
The card can be square or rectangle. It should be double sided.
I prefer 1-2 colors (not too colorful - but using color an an accent) Even if using color on the edges as an accent.

My snapgrove link shows some other graphics styles that I like. I like clean and simple.
http://www.snapgrove-boards.net/marenrosko/business-cards/

```html
<!DOCTYPE html>
<html lang="en">
<head>
<meta charset="UTF-8">
<title>MR Business Card</title>
<link href="https://fonts.googleapis.com/css2?family=Oswald:wght@300;400;600&display=swap" rel="stylesheet">
<style>
  :root {
    --magenta: #cc1c6c;
    --paper: #ffffff;
    --ink: #1f1f1f;
    --backdrop: #e9e6e1;
  }
  * { margin: 0; padding: 0; box-sizing: border-box; }
  html, body {
    width: 1200px;
    height: 1000px;
    overflow: hidden;
    background: var(--backdrop);
  }
  .stage {
    position: relative;
    width: 1200px;
    height: 1000px;
  }
  .card {
    position: absolute;
    left: 250px;
    width: 700px;
    height: 400px;
    box-shadow: 0 6px 18px rgba(0,0,0,0.18);
    font-family: 'Oswald', sans-serif;
  }
  .card-front {
    top: 70px;
    background: var(--magenta);
  }
  .card-front .front-name {
    position: absolute;
    right: 48px;
    bottom: 46px;
    color: var(--paper);
    font-weight: 600;
    font-size: 54px;
    letter-spacing: 0.5px;
    line-height: 1;
  }
  .card-back {
    top: 530px;
    background: var(--paper);
  }
  .identity {
    position: absolute;
    right: 48px;
    top: 34px;
    text-align: right;
  }
  .identity .back-name {
    color: var(--magenta);
    font-weight: 600;
    font-size: 54px;
    line-height: 1.05;
    letter-spacing: 0.5px;
  }
  .identity .studio {
    color: var(--ink);
    font-weight: 300;
    font-size: 30px;
    line-height: 1.3;
    margin-top: 4px;
    margin-right: 62px;
  }
  .identity .studio .amp { text-decoration: underline; text-underline-offset: 3px; }
  .identity .services {
    color: var(--ink);
    font-weight: 400;
    font-size: 20px;
    line-height: 1.4;
    margin-right: 10px;
  }
  .contact {
    position: absolute;
    left: 58px;
    bottom: 38px;
    list-style: none;
    color: var(--ink);
    font-weight: 300;
    font-size: 27px;
    line-height: 1.55;
  }
  .contact .label {
    color: var(--magenta);
    font-weight: 600;
    margin-right: 6px;
  }
</style>
</head>
<body>
  <main class="stage">
    <section class="card card-front" aria-label="Card front">
      <h1 class="front-name">MAREN ROSKO</h1>
    </section>
    <section class="card card-back" aria-label="Card back">
      <div class="identity">
        <h2 class="back-name">MAREN ROSKO</h2>
        <p class="studio">HOSPITALITY <span class="amp">&amp;</span> HOME</p>
        <p class="services">FF&amp;E furniture, lighting, textiles, etc.</p>
      </div>
      <ul class="contact">
        <li><span class="label">P:</span>555.014.2298</li>
        <li><span class="label">E:</span>maren@marenrosko.com</li>
      </ul>
    </section>
  </main>
</body>
</html>
```